Allied Health business card / Logo update.

Update/revitalise our logo and business cards. The logo needs to be suitable not only for business cards but stationary, website and clothing as well.

We have had the same hand logo for 16 years and have a strong brand name with this. One idea, however, was to base the idea around the similarities between the spine and bamboo. I will attach some images.

We are uncertain with colour. Initially, we thought earthy greens and greys/charcoal. However, we would also consider blue/charcoal combination.

I have attached our existing logo and this is our website. http://www.harbourleafspinal.com.au

Target Market(s)

General public
This is the only card

Industry/Entity Type

Health Care

Contact Information for Business Card

Harbourleaf Chiropractic Centre
27 Willowmere Road (Cnr Banfield St and Willowmere Rd) Seabrook Heads
4/58 Thornbury St Millbrae Vale
phone: 02 6571 4826
email: info@harbourleafspinal.com.au
web: harbourleafspinal.com.au

Marcus P. Helton
Cert. Rehab Therapist
Chiropractor
BSc(Hons)., MChirop(Clin)., MRehabNeuro(Adv)
MCHA, MANPA, VRSA

Font styles to use
Serif
Sans Serif

Colors
acd037
85acd3
5c5c5c

Requirements
Must have
• Company name, Professional name with qualifications
• Contact details.

```html
<!DOCTYPE html>
<html lang="en">
<head>
<meta charset="utf-8">
<title>Harbourleaf Chiropractic Centre – Business Card</title>
<link href="https://fonts.googleapis.com/css2?family=Open+Sans:wght@400;600&family=Vollkorn:wght@700&display=swap" rel="stylesheet">
<style>
  :root {
    --backdrop: #3d3d3f;
    --card-green: #a3d9a9;
    --card-green-light: #b3e2b8;
    --charcoal: #3c3c3c;
    --band: #3a3a3a;
    --white: #ffffff;
  }
  * { box-sizing: border-box; margin: 0; padding: 0; }
  html, body {
    width: 1200px; height: 800px; overflow: hidden;
    background: var(--backdrop);
  }
  .canvas {
    position: relative; width: 1200px; height: 800px;
    display: flex; align-items: center; justify-content: center;
  }
  .card {
    position: relative; width: 900px; height: 514px;
    background: linear-gradient(160deg, var(--card-green-light), var(--card-green));
    box-shadow: 0 10px 30px rgba(0,0,0,.35);
    overflow: hidden;
    font-family: "Open Sans", Arial, sans-serif;
    color: var(--white);
  }
  .card__texture {
    position: absolute; inset: 0;
    background: radial-gradient(ellipse at 70% 30%, rgba(255,255,255,.12), rgba(255,255,255,0) 60%);
  }
  .practitioner {
    position: absolute; left: 520px; top: 58px;
  }
  .practitioner__name {
    font-family: "Vollkorn", Georgia, serif;
    font-weight: 700; font-size: 36px; color: var(--charcoal);
    line-height: 1.1;
  }
  .practitioner__roles {
    margin-top: 6px; font-size: 24px; line-height: 1.3;
  }
  .practitioner__qualifications {
    margin-top: 26px; font-size: 20px; line-height: 1.35;
  }
  .brand {
    position: absolute; left: 110px; top: 160px;
    display: flex; align-items: center; gap: 16px;
  }
  .brand__dot {
    width: 46px; height: 46px; border-radius: 50%;
    background: var(--charcoal); flex: none;
  }
  .brand__name {
    font-weight: 600; font-size: 28px; line-height: 1.1;
    color: var(--charcoal);
  }
  .contact {
    position: absolute; right: 420px; top: 268px;
    text-align: right; font-size: 19px; line-height: 1.4;
    font-style: normal;
  }
  .address-band {
    position: absolute; left: 0; right: 0; top: 378px; height: 88px;
    background: var(--band);
    display: flex; flex-direction: column; justify-content: center;
    align-items: flex-end; padding-right: 40px;
    font-size: 19px; line-height: 1.45;
  }
</style>
</head>
<body>
<main class="canvas">
  <article class="card">
    <div class="card__texture" role="img" aria-label="Faint tonal background pattern"></div>

    <section class="practitioner">
      <h1 class="practitioner__name">Marcus P. Helton</h1>
      <p class="practitioner__roles">Cert. Rehab Therapist<br>Chiropractor</p>
      <p class="practitioner__qualifications">BSc(Hons)., MChirop(Clin).,<br>MRehabNeuro(Adv)<br>MCHA, MANPA, VRSA</p>
    </section>

    <div class="brand">
      <span class="brand__dot"></span>
      <p class="brand__name">Harbourleaf<br>Chiropractic Centre</p>
    </div>

    <address class="contact">
      02 6571 4826<br>
      info@harbourleafspinal.com.au<br>
      www.harbourleafspinal.com.au
    </address>

    <div class="address-band">
      <span>27 Willowmere Road (Cnr Banfield St and Willowmere Rd), Seabrook Heads</span>
      <span>4/58 Thornbury St Millbrae Vale</span>
    </div>
  </article>
</main>
</body>
</html>
```